Honolulu based car rental and retail shop needs a business card

We need a card design for an established company in Honolulu called Coral Motor Exchange. We rent cars mainly to tourists and visitors through an app called Veska. (Veska is not ours)- We also retail cars at the same location... The card should communicate a modern island/tropical feel. I have my website in limbo with a old "friend".. So for now we'll omit the web info until I can regain control of the site. We can also use a small version of the Veska logo to go with the account info.

Target Market(s)

Walk in and client meetings

Contact Information for Business Card

I need to have address, ph #, email, and I'd love to have a highlighted section with my Veska act. info.

Logo Text

Coral Motor Exchange

Font styles to use
Serif

Colors
3276b5
ffffff
faa54b
fcca95
eaf1f7

Requirements
Must have
• Derek Holloway
• email: derek@coralmotorhire.example
• Ph# 808-555-0147
• Address: 4175 Mahina Ln. Honolulu, Hi 96813
• Veska: https://veskadrive.example/en-us/drivers/5031476
Nice to have
• To Rent: https://veskadrive.example/en-us/drivers/5031476
• To Buy: 4175 Mahina Ln. Honolulu Hi 96813
• Maybe some suggestions here would be nice too! Maybe double sided?

```html
<!DOCTYPE html>
<html lang="en">
<head>
<meta charset="utf-8">
<title>Coral Motor Exchange — Business Card</title>
<link rel="stylesheet" href="https://fonts.googleapis.com/css2?family=Questrial&family=Roboto+Condensed:wght@600&display=swap">
<style>
  :root {
    --page-bg: #eaf1f7;
    --card-white: #ffffff;
    --brand-blue: #3276b5;
    --sun-orange: #faa54b;
    --sand: #fcca95;
    --ink: #1d1d1d;
  }
  * { margin: 0; padding: 0; box-sizing: border-box; }
  html, body { width: 900px; height: 1200px; overflow: hidden; }
  body {
    position: relative;
    background: var(--page-bg);
    font-family: "Questrial", "Century Gothic", sans-serif;
    color: var(--ink);
  }
  .card {
    position: absolute;
    background: var(--card-white);
    border-radius: 18px;
    overflow: hidden;
    box-shadow: 0 6px 16px rgba(0,0,0,0.22);
  }
  .card-front { left: 78px; top: 136px; width: 762px; height: 434px; }
  .card-back  { left: 76px; top: 630px; width: 766px; height: 436px; }
  .card-wave { position: absolute; inset: 0; width: 100%; height: 100%; }

  .holder-name {
    position: absolute; left: 44px; top: 54px;
    font-family: "Roboto Condensed", "Arial Narrow", sans-serif;
    font-weight: 600; font-size: 29px; letter-spacing: 0.3px;
    color: var(--brand-blue);
    text-transform: uppercase;
  }
  .contact-lines {
    position: absolute; left: 44px; top: 132px;
    font-size: 18.5px; line-height: 26px; letter-spacing: 0.4px;
  }
  .contact-lines .address { margin-top: 17px; }

  .brand-name {
    position: absolute;
    font-family: "Questrial", "Century Gothic", sans-serif;
    color: var(--brand-blue);
    text-align: center; line-height: 1.05;
  }
  .card-front .brand-name { left: 410px; top: 70px; width: 320px; font-size: 44px; }
  .card-back .brand-name { left: 130px; top: 72px; width: 506px; font-size: 78px; }

  .rental-partner {
    position: absolute; left: 34px; top: 352px;
    display: flex; align-items: center; gap: 8px;
    width: 134px; height: 46px; padding-left: 12px;
    border: 2px solid var(--ink); border-radius: 3px;
    font-size: 24px; letter-spacing: 1px;
  }
  .rental-partner .mark { width: 10px; height: 10px; background: var(--ink); }
  .booking-info {
    position: absolute; left: 183px; top: 350px;
    font-size: 18.5px; line-height: 26px; letter-spacing: 0.3px;
  }
  .booking-info strong { font-family: "Roboto Condensed", "Arial Narrow", sans-serif; font-weight: 600; }
</style>
</head>
<body>

  <section class="card card-front">
    <svg class="card-wave" viewBox="0 0 762 434" preserveAspectRatio="none" aria-hidden="true">
      <path d="M0,328 Q381,247 762,338 L762,434 L0,434 Z" fill="var(--sun-orange)"/>
      <path d="M0,322 Q381,241 762,332" fill="none" stroke="var(--brand-blue)" stroke-width="7"/>
    </svg>
    <h1 class="holder-name">Derek Holloway</h1>
    <div class="contact-lines">
      <p>Ph# 808-555-0147</p>
      <p>derek@coralmotorhire.example</p>
      <p class="address">4175 Mahina<br>Ln. Honolulu, Hi 96813</p>
    </div>
    <p class="brand-name">Coral Motor<br>Exchange</p>
    <div class="rental-partner"><span class="mark"></span>VESKA</div>
    <div class="booking-info">
      <p><strong>To Rent:</strong> https://veskadrive.example/en-us/drivers/5031476</p>
      <p><strong>To Buy:</strong> Visit 4175 Mahina Ln. Honolulu Hi 96813</p>
    </div>
  </section>

  <section class="card card-back">
    <svg class="card-wave" viewBox="0 0 766 436" preserveAspectRatio="none" aria-hidden="true">
      <path d="M0,394 Q383,305 766,401 L766,436 L0,436 Z" fill="var(--sun-orange)"/>
      <path d="M0,388 Q383,299 766,395" fill="none" stroke="var(--brand-blue)" stroke-width="7"/>
    </svg>
    <p class="brand-name">Coral Motor<br>Exchange</p>
  </section>

</body>
</html>
```